Business Card Design Project

New business cards that encompass our new logo.
Looking for -
Name, Title, Cell Phone, Email, Address (2 lines), Main Phone, Fax, and website.
Reason: I don't like the graphics used to show phone, fax, cell, email, web, and address.....
I like the double sided cards with logo's on the back. I do not like the logos for phone, fax, cell, address, email, or web.

```html
<!DOCTYPE html>
<html lang="en">
<head>
<meta charset="utf-8">
<title>Northpeak Restaurant Supply – Business Cards</title>
<link href="https://fonts.googleapis.com/css2?family=Montserrat:wght@700&family=Didact+Gothic&display=swap" rel="stylesheet">
<style>
  :root {
    --page-bg: #e6e8ea;
    --card-white: #ffffff;
    --brand-blue: #1d4690;
    --brand-red: #d83a3f;
    --text-grey: #555a60;
    --steel-light: #d9dde0;
    --steel-dark: #6f757b;
    --food-warm: #b07a3c;
    --food-dark: #3a3530;
  }
  * { box-sizing: border-box; margin: 0; padding: 0; }
  html, body { width: 1200px; height: 1000px; overflow: hidden; }
  body {
    background: var(--page-bg);
    font-family: "Didact Gothic", "Century Gothic", sans-serif;
    display: flex;
    align-items: center;
    justify-content: center;
    gap: 50px;
  }
  .card {
    position: relative;
    width: 525px;
    height: 300px;
    background: var(--card-white);
    overflow: hidden;
    box-shadow: 0 10px 30px rgba(0,0,0,0.18);
  }
  .brand-name {
    font-family: "Montserrat", sans-serif;
    font-weight: 700;
    color: var(--brand-blue);
    text-transform: uppercase;
    line-height: 1.05;
  }

  /* Front */
  .front .photo-kitchen {
    position: absolute;
    top: 0; right: 0;
    width: 215px; height: 100%;
    background: linear-gradient(160deg, var(--steel-light) 0%, #aeb4b9 45%, var(--steel-dark) 100%);
  }
  .front .brand-name {
    position: absolute;
    top: 48px; left: 34px;
    font-size: 30px;
  }
  .front .brand-name small { display: block; font-size: 13px; letter-spacing: 1px; }
  .front .contact-band {
    position: absolute;
    top: 140px; left: 0;
    width: 100%; height: 72px;
    background: var(--brand-blue);
    color: var(--card-white);
  }
  .person {
    position: absolute;
    top: 14px; left: 34px;
  }
  .person-name { color: var(--brand-red); font-size: 22px; }
  .person-title { font-size: 14px; margin-top: 2px; }
  .direct {
    position: absolute;
    top: 16px; left: 330px;
    font-size: 14px;
    line-height: 1.45;
  }
  .direct .mobile { font-size: 16px; font-family: "Montserrat", sans-serif; font-weight: 700; }
  .office-lines {
    position: absolute;
    top: 228px; left: 330px;
    color: var(--card-white);
    font-size: 14px;
    line-height: 1.5;
  }
  .office-lines .label { color: var(--brand-red); }
  .address {
    position: absolute;
    top: 232px; left: 34px;
    color: var(--text-grey);
    font-size: 15px;
    line-height: 1.4;
  }

  /* Back */
  .back .brand-name {
    position: absolute;
    top: 52px; left: 0;
    width: 100%;
    text-align: center;
    font-size: 40px;
  }
  .back .brand-name small { display: block; font-size: 17px; letter-spacing: 1.5px; margin-top: 4px; }
  .back .photo-buffet {
    position: absolute;
    bottom: 0; left: 0;
    width: 100%; height: 118px;
    background: linear-gradient(100deg, var(--food-dark) 0%, var(--food-warm) 50%, #8a6a45 75%, var(--food-dark) 100%);
  }
  .back .web-band {
    position: absolute;
    top: 192px; left: 0;
    width: 100%; height: 30px;
    background: var(--brand-blue);
    color: var(--card-white);
    font-size: 16px;
    letter-spacing: 1px;
    display: flex;
    align-items: center;
    justify-content: center;
  }
</style>
</head>
<body>
  <section class="card front" aria-label="Card front">
    <div class="photo-kitchen" role="img" aria-label="Photo of a stainless steel commercial kitchen"></div>
    <div class="brand-name">Northpeak<small>Restaurant Supply</small></div>
    <div class="contact-band">
      <div class="person">
        <div class="person-name">Jordan Ellis</div>
        <div class="person-title">Accountant</div>
      </div>
      <div class="direct">
        <div class="mobile">070 555 0182</div>
        <div>jordan@northpeak.com</div>
      </div>
    </div>
    <div class="office-lines">
      <div><span class="label">T+</span> 84 5550 1234</div>
      <div><span class="label">F+</span> 84 5550 5678</div>
    </div>
    <address class="address" style="font-style:normal">
      48 Harbour Lane<br>Westfield Bristol BS8
    </address>
  </section>

  <section class="card back" aria-label="Card back">
    <div class="brand-name">Northpeak<small>Restaurant Supply</small></div>
    <div class="photo-buffet" role="img" aria-label="Photo of a buffet counter with hot food trays"></div>
    <div class="web-band">www.northpeak.com</div>
  </section>
</body>
</html>
```